Infographic Illustration Design Project

We need an infographic fo a foundation based in Vancouver, BC, Canada.
We need it to be bold and colourful and show what we've done as a foundation over the last year.
Here is the content needed to put into the infographic:
BRIGHT HARBOR FOUNDATION
INFOGRAPHIC
www.brightharborfdn.org
Top section
Image: Map of the world
Text: Where Bright Harbor Foundation is Investing
(see image here for where to pins on the map of the world) http://www.brightharborfdn.org/about/about.aspx?page=2
Next section
What is the Bright Harbor Foundation Providing for Missionaries?
Image: Video camera
Text in video camera image: 82
82 Video Cameras Shipwaved Overseas
Image: Web Page
Text in web page: 116
116 Web Pages Created
Image: Dollar Bill
Text in Dollar Bill: $6,000
$6,000 in Matching Funds
Image: E-Mail
Text in E-Mail: 67
67 Fundraising Training E-Letters Sent
Missionaries Telling their Story
Image: Vidstream Video
Text: 110
110 Videos Uploaded from the Field
Image: Cell phone
Text 214
214 Text Messages Sent from the Field
Image: Poloroid photo
Text: 580
580 Photos Uploaded from the Field
Funds were raised
In MASSIVE text: $331,291.55
smaller text: Raised for Missionaries and Wired Overseas
Through various ways
Image: beer glass
Text: 1
1 Champion Who Gave Up Beer to Raise Money for Missions
Image: Wedding Cake Topper
Text: 1
1 Champion Who Gave Up their Wedding to Raise Money for Missions
Image: Birthday Present
Text: 1
1 Champion who Gave up Their Birthday to Raise Money for Missions
Image: People
Text 83
83 People Who Have Fundraised for a Missionary
*Stats are up to date as of Nov, 2012
Our website: www.brightharborfdn.org
Target Market(s)
18-60 year olds who have given to the foundation
Industry/Entity Type
Camera
Look and feel

```html
<!DOCTYPE html>
<html lang="en">
<head>
<meta charset="utf-8">
<title>Bright Harbor Foundation Infographic</title>
<link rel="stylesheet" href="https://fonts.googleapis.com/css2?family=Arimo:wght@400;700&display=swap">
<style>
  :root{
    --bg-top:#4f7fa0;
    --bg-mid:#2f5d7e;
    --bg-deep:#1c3e58;
    --panel:rgba(255,255,255,0.07);
    --panel-line:rgba(255,255,255,0.28);
    --head-bar:rgba(120,175,210,0.35);
    --white:#ffffff;
    --orange:#f08a1c;
    --lime:#b3c91d;
    --yellow:#f1c21b;
    --red:#c4262e;
    --ink:#3a3a3a;
    --footer:#1a3a52;
  }
  *{margin:0;padding:0;box-sizing:border-box}
  html,body{width:1200px;height:3000px;overflow:hidden}
  body{
    font-family:"Arimo",Arial,sans-serif;
    color:var(--white);
    background:linear-gradient(180deg,var(--bg-top) 0%,var(--bg-mid) 35%,var(--bg-mid) 75%,var(--bg-deep) 100%);
    position:relative;
  }
  .block{position:absolute;left:0;width:1200px}
  .masthead{top:30px;text-align:center}
  .masthead h1{font-size:62px;font-weight:700;letter-spacing:2px}
  .masthead .url{font-size:38px;font-weight:700;margin-top:8px}
  .world{top:190px;height:600px}
  .world-map{
    position:absolute;left:60px;top:0;width:900px;height:520px;
    background:radial-gradient(ellipse at 45% 45%,#d8e6ef 0%,#a9c3d6 45%,rgba(120,160,190,0) 75%);
    border-radius:40px;
  }
  .world-brand{position:absolute;right:70px;top:170px;font-size:44px;font-weight:700}
  .world-caption{position:absolute;left:0;width:1200px;top:540px;text-align:center;font-size:32px;font-weight:700}
  .panel{
    background:var(--panel);
    border-top:3px solid var(--panel-line);
    border-bottom:3px solid var(--panel-line);
    padding:0 50px;
  }
  .panel-title{
    margin:22px 0 30px;background:var(--head-bar);
    font-size:29px;font-weight:700;text-align:center;padding:16px 0;white-space:nowrap;
  }
  .panel-title.plain{background:none;padding:10px 0;margin-bottom:20px;font-size:36px}
  .stats{display:flex;justify-content:space-around}
  .stat{width:230px;text-align:center}
  .stat svg{display:block;margin:0 auto 16px}
  .stat p{font-size:25px;font-weight:700;line-height:1.2;hyphens:none}
  .providing{top:830px;height:480px}
  .story{top:1340px;height:440px}
  .funds{top:1810px;height:380px}
  .funds .raise{display:flex;align-items:center;justify-content:center;gap:30px;margin-top:10px}
  .funds .amount{font-size:150px;font-weight:700;letter-spacing:-2px}
  .funds .sub{text-align:center;font-size:36px;font-weight:700;margin-top:10px}
  .champions{top:2220px;height:520px}
  .footnote{position:absolute;top:2762px;left:0;width:1200px;text-align:center;font-size:22px}
  .hands{
    position:absolute;top:2805px;left:0;width:1200px;height:135px;
    background:linear-gradient(90deg,var(--red),var(--orange),var(--lime),var(--yellow),var(--red),var(--orange),var(--lime));
    border-radius:70px 70px 0 0;opacity:.9;
  }
  .footer{
    position:absolute;top:2940px;left:0;width:1200px;height:60px;background:var(--footer);
    text-align:center;font-size:34px;font-weight:700;line-height:60px;
  }
  .num{font-family:"Arimo",Arial,sans-serif;font-weight:700}
</style>
</head>
<body>

<header class="block masthead">
  <h1>BRIGHT HARBOR FOUNDATION</h1>
  <div class="url">www.brightharborfdn.org</div>
</header>

<section class="block world">
  <div class="world-map" role="img" aria-label="World map with pins marking the countries where Bright Harbor Foundation invests"></div>
  <div class="world-brand">Bright Harbor</div>
  <div class="world-caption">Where Bright Harbor Foundation is Investing</div>
</section>

<section class="block panel providing">
  <h2 class="panel-title">What is the Bright Harbor Foundation Providing for Missionaries?</h2>
  <div class="stats">
    <div class="stat">
      <svg width="150" height="150" viewBox="0 0 150 150"><rect width="150" height="150" rx="16" fill="var(--orange)"/><rect x="28" y="48" width="76" height="56" rx="6" fill="#fff"/><polygon points="104,62 128,50 128,102 104,90" fill="#fff"/><text x="66" y="88" text-anchor="middle" font-size="32" class="num" fill="var(--ink)">82</text></svg>
      <p>82 Video Cameras Shipwaved Overseas</p>
    </div>
    <div class="stat">
      <svg width="150" height="150" viewBox="0 0 150 150"><rect width="150" height="150" rx="16" fill="var(--lime)"/><rect x="25" y="30" width="100" height="90" rx="4" fill="#fff"/><rect x="25" y="30" width="100" height="14" fill="#d9d9d9"/><text x="75" y="94" text-anchor="middle" font-size="32" class="num" fill="var(--ink)">116</text></svg>
      <p>116 Web Pages Created</p>
    </div>
    <div class="stat">
      <svg width="150" height="150" viewBox="0 0 150 150"><rect width="150" height="150" rx="16" fill="var(--yellow)"/><rect x="14" y="45" width="122" height="60" rx="6" fill="#fff"/><text x="75" y="87" text-anchor="middle" font-size="30" class="num" fill="var(--ink)">$6000</text></svg>
      <p>$6,000 in Matching Funds</p>
    </div>
    <div class="stat">
      <svg width="150" height="150" viewBox="0 0 150 150"><rect width="150" height="150" rx="16" fill="var(--red)"/><rect x="24" y="36" width="102" height="78" fill="#fff"/><polyline points="24,36 75,78 126,36" fill="none" stroke="#ccc" stroke-width="3"/><text x="75" y="100" text-anchor="middle" font-size="32" class="num" fill="var(--ink)">67</text></svg>
      <p>67 Fundraising Training E&#8209;Letters Sent</p>
    </div>
  </div>
</section>

<section class="block panel story">
  <h2 class="panel-title">Missionaries Telling their Story</h2>
  <div class="stats">
    <div class="stat">
      <svg width="150" height="150" viewBox="0 0 150 150"><rect width="150" height="150" rx="16" fill="#fff"/><text x="75" y="62" text-anchor="middle" font-size="36" class="num" fill="var(--ink)">110</text><text x="75" y="106" text-anchor="middle" font-size="24" class="num" fill="var(--red)">Vidstream</text></svg>
      <p>110 Videos Uploaded from the Field</p>
    </div>
    <div class="stat">
      <svg width="150" height="150" viewBox="0 0 150 150"><rect width="150" height="150" rx="16" fill="var(--lime)"/><rect x="45" y="18" width="60" height="114" rx="10" fill="#fff"/><rect x="52" y="32" width="46" height="60" fill="#e6e6e6"/><text x="75" y="71" text-anchor="middle" font-size="24" class="num" fill="var(--ink)">214</text><circle cx="75" cy="114" r="7" fill="#ccc"/></svg>
      <p>214 Text Messages Sent from the Field</p>
    </div>
    <div class="stat">
      <svg width="150" height="150" viewBox="0 0 150 150"><rect width="150" height="150" rx="16" fill="var(--red)"/><rect x="28" y="22" width="94" height="106" fill="#fff"/><rect x="36" y="30" width="78" height="72" fill="#e6e6e6"/><text x="75" y="77" text-anchor="middle" font-size="30" class="num" fill="var(--ink)">580</text></svg>
      <p>580 Photos Uploaded from the Field</p>
    </div>
  </div>
</section>

<section class="block panel funds">
  <h2 class="panel-title plain">Funds were raised</h2>
  <div class="raise">
    <svg width="180" height="150" viewBox="0 0 180 150" aria-hidden="true"><rect x="10" y="110" width="26" height="36" fill="#fff"/><rect x="46" y="90" width="26" height="56" fill="#fff"/><rect x="82" y="70" width="26" height="76" fill="#fff"/><rect x="118" y="50" width="26" height="96" fill="#fff"/><polyline points="10,95 60,65 95,80 150,25" fill="none" stroke="#fff" stroke-width="10"/><polygon points="135,10 175,5 165,45" fill="#fff"/></svg>
    <div class="amount">$331,291.55</div>
  </div>
  <div class="sub">Raised for Missionaries and Wired Overseas</div>
</section>

<section class="block panel champions">
  <h2 class="panel-title">What is the Bright Harbor Foundation Providing for Missionaries?</h2>
  <div class="stats">
    <div class="stat">
      <svg width="150" height="150" viewBox="0 0 150 150"><rect width="150" height="150" rx="16" fill="var(--orange)"/><rect x="40" y="30" width="60" height="96" rx="6" fill="#fff"/><path d="M100 50 h16 a8 8 0 0 1 8 8 v34 a8 8 0 0 1 -8 8 h-16" fill="none" stroke="#fff" stroke-width="8"/><text x="70" y="90" text-anchor="middle" font-size="34" class="num" fill="var(--ink)">1</text></svg>
      <p>1 Champion Who Gave Up Beer to Raise Money for Missions</p>
    </div>
    <div class="stat">
      <svg width="150" height="150" viewBox="0 0 150 150"><rect width="150" height="150" rx="16" fill="var(--lime)"/><rect x="30" y="100" width="90" height="26" fill="#fff"/><rect x="42" y="72" width="66" height="26" fill="#fff"/><rect x="54" y="44" width="42" height="26" fill="#fff"/><text x="75" y="94" text-anchor="middle" font-size="24" class="num" fill="var(--ink)">1</text></svg>
      <p>1 Champion Who Gave Up their Wedding to Raise Money for Missions</p>
    </div>
    <div class="stat">
      <svg width="150" height="150" viewBox="0 0 150 150"><rect width="150" height="150" rx="16" fill="var(--yellow)"/><rect x="32" y="56" width="86" height="70" fill="#fff"/><rect x="26" y="42" width="98" height="18" fill="#fff"/><text x="75" y="104" text-anchor="middle" font-size="32" class="num" fill="var(--ink)">1</text></svg>
      <p>1 Champion who Gave up Their Birthday to Raise Money for Missions</p>
    </div>
    <div class="stat">
      <svg width="150" height="150" viewBox="0 0 150 150"><rect width="150" height="150" rx="16" fill="var(--red)"/><circle cx="50" cy="58" r="16" fill="#fff"/><circle cx="100" cy="58" r="16" fill="#fff"/><path d="M22 116 a28 28 0 0 1 56 0z M72 116 a28 28 0 0 1 56 0z" fill="#fff"/><circle cx="75" cy="70" r="28" fill="#fff"/><text x="75" y="81" text-anchor="middle" font-size="28" class="num" fill="var(--red)">83</text></svg>
      <p>83 People Who Have Fundraised for a Missionary</p>
    </div>
  </div>
</section>

<p class="footnote">*Stats are up to date as of Nov, 2012</p>

<div class="hands" role="img" aria-label="Row of raised hands in red, orange, lime and yellow"></div>

<footer class="footer">www.brightharborfdn.org</footer>

</body>
</html>
```